BUSINESS CARD - HALVERDINE RURAL SERVICES

I would like to create a business card for my fertilizer spreading business. I would like to incorporate my existing logo and also a description of the services offered. The business card will be given to farmers so must be kept simple but effective. It will also be left in stores so much also be eye catching in order to stand out from other cards.

Target Market(s)

FARMERS

Requirements
Must have
• FRONT OF CARD = EXISTING LOGO + "CUSTOMISED SPREADING" below the logo

REAR Of CARD = SERVICES OFFERED AND CONTACT DETAILS

- Bulk fertilizer including Lime, Gypsum, Manure & Compost
- Granular fertilizer including Single Super, Urea, Gran-am, & Custom Blends
- Modern equipment - Autosteer & Variable Rate Capable
- Friendly & Reliable Service
- Contact Gus: 0471 502 318
Nice to have
• utilize same color scheme as existing logo

```html
<!DOCTYPE html>
<html lang="en">
<head>
<meta charset="utf-8">
<title>Halverdine Rural Services – Business Card</title>
<link href="https://fonts.googleapis.com/css2?family=Nunito:wght@400;600;700&display=swap" rel="stylesheet">
<style>
  :root {
    --backdrop: #adb4be;
    --card: #ffffff;
    --charcoal: #58585a;
    --text: #5a5a5c;
    --orange: #f7941d;
  }
  html, body {
    margin: 0;
    padding: 0;
    width: 1200px;
    height: 1200px;
    overflow: hidden;
    background: var(--backdrop);
    font-family: "Nunito", sans-serif;
  }
  .card {
    position: absolute;
    left: 264px;
    width: 672px;
    height: 403px;
    background: var(--card);
  }
  .card--back { top: 172px; }
  .card--front { top: 614px; }

  .contact-band {
    position: absolute;
    left: 0;
    top: 56px;
    width: 100%;
    height: 41px;
    background: var(--charcoal);
    color: #fff;
    font-size: 20px;
    font-weight: 600;
  }
  .contact-band__name {
    position: absolute;
    right: 406px;
    top: 50%;
    transform: translateY(-50%);
  }
  .contact-band__phone {
    position: absolute;
    left: 400px;
    top: 50%;
    transform: translateY(-50%);
  }
  .phone-badge {
    position: absolute;
    left: 300px;
    top: 42px;
    width: 72px;
    height: 72px;
  }

  .services {
    position: absolute;
    left: 46px;
    top: 140px;
    color: var(--text);
  }
  .services__title {
    margin: 0 0 12px;
    font-size: 22px;
    font-weight: 700;
    letter-spacing: 0.3px;
  }
  .services__list {
    list-style: none;
    margin: 0;
    padding: 0;
    font-size: 17px;
    line-height: 29px;
  }
  .services__list li {
    position: relative;
    padding-left: 25px;
  }
  .services__list li::before {
    content: "";
    position: absolute;
    left: 0;
    top: 10px;
    width: 9px;
    height: 9px;
    border-radius: 50%;
    background: var(--orange);
  }

  .back-mark {
    position: absolute;
    right: 30px;
    bottom: 30px;
  }
  .back-mark__dot {
    display: block;
    width: 64px;
    height: 64px;
    border-radius: 50%;
    background: var(--charcoal);
  }

  .brand {
    position: absolute;
    left: 0;
    top: 76px;
    width: 100%;
    display: flex;
    flex-direction: column;
    align-items: center;
  }
  .brand__dot {
    width: 168px;
    height: 168px;
    border-radius: 50%;
    background: var(--charcoal);
  }
  .brand__name {
    margin-top: 8px;
    font-size: 34px;
    font-weight: 700;
    line-height: 44px;
    color: var(--charcoal);
  }
  .brand__tagline {
    margin-top: 4px;
    font-size: 17px;
    font-weight: 700;
    letter-spacing: 3px;
    color: var(--orange);
  }
</style>
</head>
<body>

  <section class="card card--back">
    <div class="contact-band">
      <span class="contact-band__name">Contact Gus</span>
      <span class="contact-band__phone">0471 502 318</span>
    </div>
    <svg class="phone-badge" viewBox="0 0 72 72" aria-hidden="true">
      <circle cx="36" cy="36" r="34" fill="var(--charcoal)"/>
      <circle cx="36" cy="36" r="29" fill="var(--orange)"/>
      <path d="M27 23c2-1 3 0 4 2l2 4c1 2 0 3-1 4l-1 1c1 3 4 6 7 7l1-1c1-1 2-2 4-1l4 2c2 1 3 2 2 4-1 3-4 5-7 4-8-2-15-9-17-17-1-3 1-8 2-9z" fill="#fff"/>
    </svg>

    <div class="services">
      <h2 class="services__title">SERVICES OFFERED</h2>
      <ul class="services__list">
        <li>Bulk fertilizer including Lime, Gypsum, Manure &amp; Compost</li>
        <li>Granular fertilizer including Single Super, Urea,<br>Gran-am, &amp; Custom Blends</li>
        <li>Modern equipment - Autosteer &amp; Variable Rate Capable</li>
        <li>Friendly &amp; Reliable Service</li>
      </ul>
    </div>

    <div class="back-mark">
      <span class="back-mark__dot"></span>
    </div>
  </section>

  <section class="card card--front">
    <div class="brand">
      <span class="brand__dot"></span>
      <span class="brand__name">Halverdine Rural Services</span>
      <span class="brand__tagline">CUSTOMISED SPREADING</span>
    </div>
  </section>

</body>
</html>
```